Free range pig farm business

We'd like a simple but elegant website for our new free range pig farm business.
Check out www.tallowcreekporkers.com.au and http://www.quorrihollow.com.au/
pages:
Home
About
Shop
Contact
Target Market(s)
People who would want to find out where they could buy our pork
Industry/Entity Type
Agribusiness
Number of Pages Required
4 page
Font styles to use
Other font styles liked:
- As per our logo
Requirements
Must have
- Ability for us to update weekly with new news and photos

```html
<!DOCTYPE html>
<html lang="en">
<head>
<meta charset="utf-8">
<title>Ridgeline Free Range Pork</title>
<link href="https://fonts.googleapis.com/css2?family=Roboto:wght@300;400;500;700&display=swap" rel="stylesheet">
<style>
:root{
  --green:#8bae2e;
  --green-dark:#6f921d;
  --green-light:#a8c64a;
  --olive-text:#3d4a1c;
  --bar:#3a3a3a;
  --header-grey:#e7eae4;
  --panel:#d9e1bf;
  --field:#f2f2f2;
  --text:#555;
  --footer:#f3f3f3;
  --white:#fff;
}
*{margin:0;padding:0;box-sizing:border-box}
html,body{width:1200px;height:2206px;overflow:hidden}
body{position:relative;background:var(--white);font-family:'Roboto',sans-serif;color:var(--text)}
.abs{position:absolute}
.top-bar{left:0;top:0;width:1200px;height:19px;background:var(--bar);font-size:9px;color:#ddd;line-height:19px}
.top-bar .note{left:184px}
.top-bar .note em{font-style:normal;color:#c4d94a}
.top-bar .phone{left:924px;color:#c4d94a}
.header-bg{left:0;top:19px}
.nav-ribbon{left:162px;top:74px}
.nav-link{top:88px;font-size:12px;color:#fff}
.home-dot{left:246px;top:80px;width:31px;height:31px;border-radius:50%;background:#4d6a1c}
.brand{left:527px;top:27px;width:146px;height:146px;border-radius:50%;background:#fff;border:2px solid #e1e5d9;display:flex;align-items:center;justify-content:center;text-align:center;padding:0 14px}
.brand span{font-size:12px;font-weight:500;color:var(--olive-text);line-height:1.3}
.slider{left:160px;top:126px}
.slider-arrow{width:45px;height:47px;background:#d8dbd4;display:flex;align-items:center;justify-content:center}
.caption{left:228px;top:350px;width:368px;height:94px;background:rgba(168,198,74,.82);padding:14px 22px;color:#fff}
.caption .lead{font-size:38px;font-weight:300;line-height:1}
.caption .sub{font-size:22px;font-weight:300;margin-top:6px}
.caption .sub b{font-weight:400;color:#3d4a1c}
.welcome{left:0;top:572px;width:1200px;text-align:center;font-size:25px;color:var(--olive-text)}
.welcome b{font-weight:500}
.intro{left:220px;top:618px;width:760px;text-align:center;font-size:10.5px;line-height:18px;color:#666}
.btn{background:linear-gradient(var(--green-light),var(--green-dark));color:#fff;font-size:15px;text-align:center;border-bottom:3px solid #5b7a16}
.section-title{left:0;width:1200px;text-align:center;font-size:24px;color:var(--olive-text)}
.section-title b{font-weight:500}
.tile{top:810px;height:280px}
.tile-overlay{display:flex;flex-direction:column;align-items:center;justify-content:center;color:#fff}
.tile-actions{display:flex;gap:12px}
.tile-action{display:flex;flex-direction:column;align-items:center;font-size:8px;font-weight:500}
.tile-action i{width:54px;height:54px;border-radius:50%;background:rgba(255,255,255,.35);margin-bottom:8px;display:flex;align-items:center;justify-content:center}
.price{font-size:27px;font-weight:500;letter-spacing:4px;margin-top:34px}
.newsletter{left:0;top:1250px;width:1200px;height:291px;background:linear-gradient(90deg,#4f7a2c,#6b8f3c 40%,#5a8432);}
.newsletter-frame{left:14px;top:1268px;width:1172px;height:255px;border:1px dashed rgba(255,255,255,.35)}
.newsletter-title{left:157px;top:1338px;font-size:31px;font-weight:300;color:#fff}
.newsletter-title b{font-weight:500}
.email-box{left:159px;top:1404px;width:473px;height:45px;background:#fff;border:3px solid #fff;outline:1px solid #ccc}
.email-box span{position:absolute;left:14px;top:12px;font-size:12px;color:#333}
.email-box .join{position:absolute;right:0;top:0;width:115px;height:39px;line-height:36px}
.pig-photo{left:672px;top:1219px;width:365px;height:381px;background:linear-gradient(160deg,#3a2a1c,#8a5a3e 45%,#c9967a 60%,#4a3424)}
.location-title{left:196px;top:1630px;font-size:23px;color:#333}
.info{font-size:10.5px;color:#444}
.map{left:194px;top:1754px;width:453px;height:280px;background:linear-gradient(90deg,#ece8de 0%,#e6e7d6 55%,#bfd99a 70%,#a9cfe9 85%,#a3cdf0 100%)}
.contact-panel{left:672px;top:1600px;width:365px;height:434px;background:var(--panel)}
.contact-title{left:672px;top:1644px;width:365px;text-align:center;font-size:23px;color:var(--olive-text)}
.field{left:706px;width:297px;background:var(--field);font-size:10.5px;color:#555;padding:12px 22px}
.footer{left:0;top:2051px;width:1200px;height:155px;background:var(--footer)}
.social{top:2084px;width:35px;height:35px;border:1px solid #ddd;background:#fff}
.footer-links{left:0;top:2133px;width:1200px;text-align:center;font-size:10.5px;color:#444;word-spacing:0}
.footer-links span{margin:0 9px}
.copyright{left:0;top:2166px;width:1200px;text-align:center;font-size:11px;color:#666}
</style>
</head>
<body>

<div class="abs top-bar">
  <span class="abs note">Neque porro quisquam est qui dolorem ipsum quia dolor sit amet,<em>50% Offer for Shipping ...</em></span>
  <span class="abs phone">&#9742;&nbsp; 1-800 214 3306</span>
</div>

<svg class="abs header-bg" width="1200" height="250" viewBox="0 0 1200 250" aria-hidden="true">
  <path d="M0 0H1200V240C1000 140 800 110 600 110S200 140 0 240Z" fill="var(--header-grey)"/>
</svg>

<svg class="abs nav-ribbon" width="876" height="44" viewBox="0 0 876 44" aria-hidden="true">
  <defs><linearGradient id="rib" x1="0" y1="0" x2="0" y2="1"><stop offset="0" stop-color="#b6cf55"/><stop offset="1" stop-color="#82a526"/></linearGradient></defs>
  <path d="M0 0H876L856 22L876 44H0L20 22Z" fill="url(#rib)"/>
  <path d="M28 6H848M28 38H848" stroke="#fff" stroke-opacity=".4" stroke-dasharray="3 3"/>
</svg>
<div class="abs home-dot"></div>
<svg class="abs" style="left:254px;top:87px" width="15" height="15" viewBox="0 0 15 15" aria-hidden="true"><path d="M7.5 1L1 7H3V14H6V10H9V14H12V7H14Z" fill="#a8c64a"/></svg>
<span class="abs nav-link" style="left:311px">About Us</span>
<span class="abs nav-link" style="left:411px">Service</span>
<span class="abs nav-link" style="left:768px">Shop</span>
<span class="abs nav-link" style="left:847px">Contact</span>
<div class="abs brand"><span>Ridgeline Free Range Pork</span></div>

<svg class="abs slider" width="880" height="430" viewBox="0 0 880 430" role="img" aria-label="Photo of young piglets standing in straw inside a farm shelter">
  <defs><linearGradient id="sl" x1="0" y1="0" x2="0" y2="1"><stop offset="0" stop-color="#f2f3f0"/><stop offset=".45" stop-color="#e6c4b6"/><stop offset=".75" stop-color="#c99a4a"/><stop offset="1" stop-color="#a77a2c"/></linearGradient></defs>
  <path d="M0 0H880V330Q440 470 0 330Z" fill="#cfd3ca"/>
  <path d="M6 6H874V324Q440 454 6 324Z" fill="url(#sl)"/>
</svg>
<div class="abs slider-arrow" style="left:148px;top:279px"><svg width="10" height="14" viewBox="0 0 10 14" aria-hidden="true"><path d="M8 1L2 7L8 13" stroke="#333" stroke-width="2" fill="none"/></svg></div>
<div class="abs slider-arrow" style="left:1007px;top:279px"><svg width="10" height="14" viewBox="0 0 10 14" aria-hidden="true"><path d="M2 1L8 7L2 13" stroke="#333" stroke-width="2" fill="none"/></svg></div>
<div class="abs caption">
  <div class="lead">We are a new</div>
  <div class="sub">FREE range <b>pig farm</b> business.</div>
</div>

<h1 class="abs welcome">Welcome To <b>Ridgeline Free Range Pork</b></h1>
<p class="abs intro">Sed ut perspiciatis unde omnis iste natus error sit voluptatem accusantium doloremque laudantium, totam rem aperiam, eaque ipsa quae ab illo inventore veritatis et quasi architecto beatae vitae dicta sunt explicabo. Nemo enim ipsam voluptatem quia voluptas sit aspernatur aut odit aut fugit, sed quia consequuntur magni dolores</p>
<div class="abs btn" style="left:543px;top:688px;width:114px;height:38px;line-height:36px">READ MORE</div>

<h2 class="abs section-title" style="top:756px">Shop <b>Products</b></h2>
<div class="abs tile tile-overlay" style="left:0;width:290px;background:linear-gradient(135deg,#6f9a2a,#8db33c)" role="img" aria-label="Product photo of leafy greens with green overlay">
  <div class="tile-actions">
    <div class="tile-action"><i><svg width="20" height="18" viewBox="0 0 20 18" aria-hidden="true"><path d="M1 2H4L6 12H16L18 5H5" stroke="#fff" stroke-width="2" fill="none"/><circle cx="7" cy="15.5" r="1.6" fill="#fff"/><circle cx="15" cy="15.5" r="1.6" fill="#fff"/></svg></i>ADD TO CART</div>
    <div class="tile-action"><i><svg width="20" height="20" viewBox="0 0 20 20" aria-hidden="true"><circle cx="8" cy="8" r="6" stroke="#fff" stroke-width="2.4" fill="none"/><path d="M12.5 12.5L18 18" stroke="#fff" stroke-width="2.6"/></svg></i>DETAILS</div>
  </div>
  <div class="price">$35.00</div>
</div>
<div class="abs tile" style="left:303px;width:288px;background:linear-gradient(160deg,#f4f1ea,#c98a4a 50%,#7a4422)" role="img" aria-label="Product photo of a grilled pork chop with vegetables"></div>
<div class="abs tile" style="left:607px;width:289px;background:linear-gradient(150deg,#c46a6e,#e6b3ae 50%,#a8484e)" role="img" aria-label="Product photo of raw pork cuts"></div>
<div class="abs tile" style="left:912px;width:288px;background:linear-gradient(150deg,#5a3a26,#d9a98c 45%,#b07a58 70%,#7a4a2a)" role="img" aria-label="Product photo of sliced roast pork"></div>
<div class="abs btn" style="left:543px;top:1119px;width:114px;height:38px;line-height:36px">SHOP NOW</div>

<div class="abs newsletter" role="img" aria-label="Background photo of a pig on green grass"></div>
<div class="abs newsletter-frame"></div>
<h2 class="abs newsletter-title">Newsletter <b>Subscribe</b></h2>
<div class="abs email-box"><span>ENTER EMAIL ID</span><div class="btn join">JOIN NOW</div></div>
<div class="abs pig-photo" role="img" aria-label="Photo of a young pig in a barn"></div>

<h2 class="abs location-title">LOCATION</h2>
<svg class="abs" style="left:196px;top:1692px" width="11" height="11" viewBox="0 0 11 11" aria-hidden="true"><path d="M2 1L4 1L5 4L3.5 5Q5 7.5 6.5 8L7.5 6.5L10 7.5V9.5Q9 10.5 7 10Q2 8 1 3Q1 1.5 2 1Z" fill="#444"/></svg>
<span class="abs info" style="left:221px;top:1691px">Phone : 1-800 214 3307</span>
<svg class="abs" style="left:196px;top:1719px" width="11" height="9" viewBox="0 0 11 9" aria-hidden="true"><rect x=".5" y=".5" width="10" height="8" fill="none" stroke="#444"/><path d="M.5 .5L5.5 5L10.5 .5" fill="none" stroke="#444"/></svg>
<span class="abs info" style="left:221px;top:1717px">Email : hello@ridgelinepork.au</span>
<svg class="abs" style="left:385px;top:1690px" width="10" height="14" viewBox="0 0 10 14" aria-hidden="true"><path d="M5 0A5 5 0 0 1 10 5C10 8 5 14 5 14S0 8 0 5A5 5 0 0 1 5 0Z" fill="#222"/><circle cx="5" cy="5" r="1.8" fill="#fff"/></svg>
<span class="abs info" style="left:410px;top:1691px">Address : Ridgeline Farm, 48 Paddock Lane</span>
<span class="abs info" style="left:410px;top:1717px">Tamworth NSW 2340</span>
<div class="abs map" role="img" aria-label="Map showing the farm location in New South Wales"></div>

<div class="abs contact-panel"></div>
<h2 class="abs contact-title">CONTACT US</h2>
<div class="abs field" style="top:1693px;height:37px">NAME</div>
<div class="abs field" style="top:1747px;height:37px">EMAIL</div>
<div class="abs field" style="top:1801px;height:37px">PHONE</div>
<div class="abs field" style="top:1856px;height:88px">MESSAGE</div>
<div class="abs btn" style="left:797px;top:1963px;width:115px;height:37px;line-height:35px">SUBMIT</div>

<div class="abs footer"></div>
<div class="abs social" style="left:513px;background:var(--green);border-color:var(--green)"></div>
<div class="abs social" style="left:559px"></div>
<div class="abs social" style="left:605px"></div>
<div class="abs social" style="left:651px"></div>
<div class="abs footer-links"><span>HOME</span><span>ABOUT US</span><span>SERVICE</span><span>SHOP</span><span>CONTACT</span></div>
<div class="abs copyright">&copy; 2016. www.ridgelinepork.au</div>

</body>
</html>
```